Up to the Challenge - PPT Template with Splash Slide

We are looking for a PPT template that has 4 slides.
1. Splash slide (Creative, fun, no content, a visual representation of the theme)
2. Section header slide
3. Content Slide
4. Content Slide, another design option
The theme is 'UP to the Challenge'. The design should reflect this theme.
The colors should be in Purple (#864B99), Blue (#0A80C2), and Green (#52B054).

```html
<!DOCTYPE html>
<html lang="en">
<head>
<meta charset="utf-8">
<title>Up to the Challenge – Slide Template</title>
<link href="https://fonts.googleapis.com/css2?family=Montserrat:wght@800;900&family=Red+Hat+Display:wght@400;500;600&family=Allura&display=swap" rel="stylesheet">
<style>
  :root{
    --purple:#864B99;
    --blue:#0A80C2;
    --green:#52B054;
    --ink:#3a3a3a;
    --white:#ffffff;
    --stage:#8aaad4;
    --night:#0d2c54;
  }
  *{margin:0;padding:0;box-sizing:border-box}
  html,body{width:1200px;height:737px;overflow:hidden;background:var(--stage)}
  .canvas{position:relative;width:1200px;height:737px}
  .slide{position:absolute;width:539px;height:303px;overflow:hidden;background:var(--white);
    font-family:"Red Hat Display",Arial,sans-serif;color:var(--ink)}
  .slide svg.backdrop{position:absolute;inset:0;width:100%;height:100%}
  .slide--splash{left:50px;top:54px}
  .slide--photos{left:611px;top:54px}
  .slide--stats{left:50px;top:379px}
  .slide--section{left:611px;top:379px}

  .title{position:absolute;font-family:"Montserrat",Arial,sans-serif;font-weight:900;line-height:1;letter-spacing:-0.5px}
  .script{position:absolute;font-family:"Allura",cursive;line-height:1;color:var(--green)}

  /* splash */
  .splash-photo{position:absolute;inset:0;background:linear-gradient(180deg,#123a6b 0%,#2f6fb0 45%,#6f8fb0 70%,#1f2f48 100%)}
  .watermark{position:absolute;left:14px;font-family:"Montserrat",Arial,sans-serif;font-weight:900;font-style:italic;
    font-size:48px;line-height:1;color:rgba(255,255,255,0.07);white-space:nowrap;letter-spacing:1px}

  /* photos slide */
  .slide--photos .title{left:29px;top:44px;font-size:30px;color:var(--white)}
  .slide--photos .script{left:68px;top:62px;font-size:56px;color:var(--white)}
  .lead{position:absolute;left:29px;top:134px;width:232px;font-size:11.3px;font-weight:600;line-height:14px;color:var(--white)}
  .body-white{position:absolute;left:29px;top:184px;width:232px;font-size:11px;line-height:14px;color:var(--white)}
  .photo{position:absolute;border-radius:10px;border:4px solid}
  .photo--audience{left:283px;top:22px;width:146px;height:122px;border-color:var(--purple);transform:rotate(4deg);
    background:linear-gradient(160deg,#6b5a52,#2b2a3a)}
  .photo--hall{left:322px;top:132px;width:160px;height:148px;border-color:var(--green);transform:rotate(-4deg);
    background:linear-gradient(170deg,#7a5a40,#2a3550 55%,#1c2433)}

  /* stats slide */
  .slide--stats .title{left:28px;top:35px;font-size:29px;color:var(--ink)}
  .slide--stats .script{left:60px;top:40px;font-size:52px}
  .subhead{position:absolute;left:21px;top:129px;font-size:13px;font-weight:500}
  .body{position:absolute;left:21px;width:200px;font-size:10.6px;line-height:14px}
  .quote-box{position:absolute;left:277px;top:29px;width:154px;height:128px;border-radius:8px;background:var(--purple);
    color:var(--white);font-size:9.8px;line-height:12.8px;padding:11px 10px}
  .stat{position:absolute;width:100px;height:80px;border-radius:7px;padding:9px 10px;box-shadow:0 3px 8px rgba(0,0,0,0.18)}
  .stat b{display:block;font-family:"Montserrat",Arial,sans-serif;font-weight:800;font-size:20px;line-height:1;margin-bottom:8px}
  .stat span{display:block;font-size:11px;line-height:14px}
  .stat--light{left:362px;top:147px;background:#f4f4f4;color:var(--ink)}
  .stat--green{left:270px;top:203px;background:var(--green);color:var(--white)}

  /* section slide */
  .slide--section .title{left:41px;top:40px;font-size:36px;color:var(--ink)}
  .slide--section .script{left:75px;top:54px;font-size:60px}
  .section-sub{position:absolute;left:41px;top:180px;font-size:18px;line-height:23px}
  .section-lines{position:absolute;left:41px;top:229px;font-size:15px;line-height:19px}
  .rocket-art{position:absolute;left:335px;top:60px;width:190px;height:240px;border-radius:20px;
    background:linear-gradient(200deg,rgba(255,255,255,0.18),rgba(255,255,255,0.06))}
</style>
</head>
<body>
<main class="canvas">

  <!-- Splash -->
  <section class="slide slide--splash">
    <div class="splash-photo" role="img" aria-label="Photo of a climber with raised arms and a small flag on a snowy mountain summit, backlit by a bright glow"></div>
    <svg class="backdrop" viewBox="0 0 539 303" aria-hidden="true">
      <polygon points="0,0 140,0 290,140 260,150" fill="var(--purple)" opacity="0.9"/>
      <polygon points="0,30 0,120 250,170 268,150" fill="var(--blue)" opacity="0.9"/>
      <polygon points="0,120 0,180 255,190 250,175" fill="var(--blue)" opacity="0.6"/>
      <polygon points="395,0 539,0 300,150 280,142" fill="var(--green)" opacity="0.92"/>
      <polygon points="539,20 539,120 330,170 305,150" fill="var(--blue)" opacity="0.9"/>
      <polygon points="539,120 539,140 340,190 335,178" fill="var(--blue)" opacity="0.6"/>
    </svg>
    <div class="watermark" style="top:10px">UP TO THE CHALLENGE</div>
    <div class="watermark" style="top:82px">UP TO THE CHALLENGE</div>
    <div class="watermark" style="top:154px">UP TO THE CHALLENGE</div>
  </section>

  <!-- Content slide with photos -->
  <section class="slide slide--photos">
    <svg class="backdrop" viewBox="0 0 539 303" aria-hidden="true">
      <polygon points="0,0 388,0 245,303 0,303" fill="var(--green)"/>
    </svg>
    <h2 class="title">SLIDE</h2>
    <div class="script">Heading</div>
    <p class="lead">Lorem ipsum dolor sit amet, consectetur adipiscing elit, sed do eiusmod tempor incididunt ut labore et dolore magna aliqua.</p>
    <p class="body-white">Lorem ipsum dolor sit amet, consectetur adipiscing elit, sed do eiusmod tempor incididunt ut labore et dolore magna aliqua. Quis ipsum suspendisse ultrices gravida. Risus commodo viverra maecenas accumsan lacus vel facilisis.</p>
    <div class="photo photo--audience" role="img" aria-label="Photo of a speaker on stage addressing a seated audience"></div>
    <div class="photo photo--hall" role="img" aria-label="Photo of a conference hall seen from behind the audience"></div>
  </section>

  <!-- Content slide with stats -->
  <section class="slide slide--stats">
    <svg class="backdrop" viewBox="0 0 539 303" aria-hidden="true">
      <polygon points="333,0 539,0 539,303 423,303" fill="var(--blue)"/>
    </svg>
    <h2 class="title">SLIDE</h2>
    <div class="script">Heading</div>
    <p class="subhead">Lorem ipsum dolor sit amet,</p>
    <p class="body" style="top:151px">Lorem ipsum dolor sit amet, consectetur adipiscing elit, sed do eiusmod tempor.</p>
    <p class="body" style="top:187px">Lorem ipsum dolor sit amet, consectetur adipiscing elit, sed do eiusmod tempor. Lorem ipsum dolor sit amet, consectetur adipiscing elit, sed do eiusmod tempor.</p>
    <div class="quote-box">Lorem ipsum dolor sit amet, consectetur adipiscing elit, sed do eiusmod tempor incididunt ut labore et dolore magna aliqua. Quis ipsum suspendisse ultrices gravida. Risus commodo viverra maecenas accumsan lacus vel facilisis.</div>
    <div class="stat stat--light"><b>65%</b><span>Lorem ipsum dolor sit amet,</span></div>
    <div class="stat stat--green"><b>65%</b><span>Lorem ipsum dolor sit amet,</span></div>
  </section>

  <!-- Section header -->
  <section class="slide slide--section">
    <svg class="backdrop" viewBox="0 0 539 303" aria-hidden="true">
      <polygon points="341,0 514,0 337,303 242,303" fill="var(--purple)"/>
      <polygon points="527,0 539,0 539,195 470,303 346,303" fill="var(--blue)"/>
    </svg>
    <div class="rocket-art" role="img" aria-label="Line illustration of a rocket launching from a ringed planet among stars"></div>
    <h2 class="title">SECTION</h2>
    <div class="script">Header</div>
    <p class="section-sub">Lorem Ipsum<br>dolor sit</p>
    <p class="section-lines">Lorem Ipsum dolor sit<br>Lorem Ipsum dolor</p>
  </section>

</main>
</body>
</html>
```